RK Cooling (logo) - Celebrating 55 Years Servicing the Chicago Suburbs. Summer is Almost Here! Make sure your system is running properly and efficiently. The industry standard recommends an A/C Clean & Check once a year.
A/C Clean & Check
Regular Preventive Maintenance Can:
-Help Prolong the Life of your Equipment
-Help Lower Your Monthly Energy Costs
-Save Costs on Future Repairs

Mention this Postcard and Take $10.00 Off
Call (555) 384-9120 I Address: 718 Birchwood Ave. Marvale, IL
_______________________________________________
BACK SIDE:
Proudly Serving Chicagoland Area Since 1961- We Also Service and Sell:
-Coastline Prime Equipment.
-Brightvane Air Cleaners & Humidifier Systems.
-Hot Water Heaters, Boilers, and Digital Thermostats.
-Residential and Commercial Fabrication. Custom Welding.

Schedule Your Spring Clean & Check Today
Phone: (555) 384-9120
Mail: rkcooling@mailnest.example
Website: www.rkcoolingair.example

I had pixel guild make a Fall Clean and Check (for furnaces) in September of 2015. Feel free too look back for ideas. The postcard needs to be creative and not the same as the fall one! Added Tuesday, March 29, 2016

Target Market(s)

HVAC Industry, Residential

Industry/Entity Type

Air Conditioning

Colors
0255a3
f6faec

Requirements
Must have
• The following text in the project description. Feel free to add more.
Nice to have
• One small picture or clipart on the front. Maybe a picture of something summery or an air conditioner.
Should not have
• No spelling mistakes. Nothing too basic.

```html
<!DOCTYPE html>
<html lang="en">
<head>
<meta charset="utf-8">
<title>RK Cooling – Spring Clean &amp; Check Postcard</title>
<link rel="stylesheet" href="https://fonts.googleapis.com/css2?family=Oswald:wght@500;700&family=Lato:ital,wght@0,400;0,700;0,900;1,700;1,900&display=swap">
<style>
  :root{
    --brand-blue:#0255a3;
    --deep-blue:#0d3f86;
    --navy:#27296b;
    --cream:#f6faec;
    --highlight:#f7f2b4;
    --oval:#f6efc6;
    --oval-edge:#d9b85a;
    --gold:#f3cf5e;
    --red:#e0201b;
    --sky:#a8daf2;
    --ink:#1d1d1f;
    --bar:#1c1c1e;
    --stage:#e8e8e3;
    --rule:#b9b9b9;
  }
  *{margin:0;padding:0;box-sizing:border-box}
  html,body{width:900px;height:1200px;overflow:hidden}
  body{background:var(--stage);position:relative;font-family:"Lato",sans-serif;color:var(--ink)}
  .card{position:absolute;left:40px;width:820px;height:540px;overflow:hidden;box-shadow:0 4px 14px rgba(0,0,0,.18)}
  .card--front{top:40px;background:linear-gradient(160deg,#ffffff 0%,#eef3f8 45%,#ffffff 100%)}
  .card--back{top:620px;background:#ffffff}
  .abs{position:absolute}

  /* front */
  .brand{left:40px;top:100px;display:flex;align-items:center;gap:10px}
  .brand__dot{width:18px;height:18px;border-radius:50%;background:var(--red)}
  .brand__name{font-family:"Oswald",sans-serif;font-weight:700;font-size:40px;color:var(--navy);line-height:1}
  .headline{left:330px;top:28px;width:470px}
  .headline__anniv{display:inline-block;background:var(--highlight);font-family:"Oswald",sans-serif;font-weight:700;font-size:30px;color:var(--brand-blue);text-transform:uppercase;padding:0 8px;line-height:1.25;white-space:nowrap}
  .headline__anniv em{font-style:normal;color:var(--red)}
  .headline__region{font-family:"Oswald",sans-serif;font-weight:700;font-size:29px;color:var(--ink);text-transform:uppercase;margin-top:2px;line-height:1.2}
  .headline__season{font-weight:900;font-size:30px;color:var(--brand-blue);margin-top:4px;line-height:1.15}
  .headline__lead{font-size:17px;margin-top:6px;line-height:1.2}
  .headline__standard{font-weight:900;font-size:17px;color:var(--red);margin-top:10px;line-height:1.2}
  .headline__standard span{color:var(--ink)}
  .benefits-band{left:330px;top:272px;width:490px;height:40px;background:var(--sky);font-weight:700;font-size:17px;color:var(--navy);padding:10px 20px}
  .benefits{left:350px;top:322px;list-style:none}
  .benefits li{font-size:16px;line-height:1.55;padding-left:20px;position:relative}
  .benefits li::before{content:"";position:absolute;left:0;top:8px;width:9px;height:9px;border-radius:50%;background:var(--brand-blue)}
  .unit-art{left:40px;top:190px;width:280px;height:230px;border-radius:6px;background:linear-gradient(150deg,#fbfbfb 0%,#dfe3e8 60%,#c5ccd4 100%)}
  .swoosh{left:0;top:0;width:820px;height:540px}
  .offer{width:240px;height:72px;border-radius:50%;background:var(--oval);border:3px solid var(--oval-edge);display:flex;align-items:center;justify-content:center;font-family:"Oswald",sans-serif;font-weight:700;font-size:34px;color:var(--ink);white-space:nowrap}
  .offer b{color:var(--red);margin-right:8px;font-weight:700}
  .offer--front{left:545px;top:402px}
  .mention{color:var(--gold);font-weight:700}
  .mention--front{left:95px;top:448px;font-size:20px}
  .contact-bar{left:0;top:490px;width:820px;height:50px;background:var(--bar);color:#fff;font-size:22px;display:flex;align-items:center;padding-left:150px;gap:8px;white-space:nowrap}
  .label{color:var(--red)}

  /* back */
  .back-panel{left:0;top:0;width:410px;height:540px;background:linear-gradient(160deg,#ffffff,#eef3f8)}
  .divider{left:410px;top:0;width:5px;height:540px;background:var(--red)}
  .since-band{left:0;top:38px;width:410px;height:32px;background:var(--highlight);font-family:"Oswald",sans-serif;font-weight:700;font-size:16px;line-height:24px;color:var(--brand-blue);text-transform:uppercase;padding:4px 16px;white-space:nowrap}
  .since-band em{font-style:normal;color:var(--red)}
  .services-title{left:25px;top:86px;font-weight:900;font-size:18px}
  .services{left:30px;top:116px;width:370px;list-style:none}
  .services li{font-size:15px;line-height:1.3;padding-left:18px;position:relative;margin-bottom:4px}
  .services li::before{content:"";position:absolute;left:0;top:6px;width:8px;height:8px;border-radius:50%;background:var(--brand-blue)}
  .offer--back{left:185px;top:298px;width:210px;height:64px;font-size:30px}
  .mention--back{left:28px;top:370px;font-size:13px;color:#fff;line-height:1.2}
  .schedule-band{left:0;top:402px;width:410px;height:40px;background:var(--cream);border-top:3px solid var(--gold);font-weight:900;font-style:italic;font-size:17px;color:var(--navy);padding:8px 22px;white-space:nowrap}
  .back-contact{left:0;top:442px;width:410px;height:98px;background:var(--brand-blue);padding:14px 28px;display:grid;grid-template-columns:78px 1fr;row-gap:2px;font-size:15px;color:#fff}
  .back-contact .label{font-weight:700}
  .stamp{left:640px;top:40px;width:130px;height:140px;background:#ececec}
  .address-line{left:465px;width:320px;height:2px;background:var(--rule)}
</style>
</head>
<body>

<section class="card card--front" aria-label="Postcard front">
  <svg class="abs swoosh" viewBox="0 0 820 540" aria-hidden="true">
    <path d="M0 330 L70 260 L120 300 L0 420 Z" fill="var(--bar)"/>
    <path d="M0 410 C200 470 420 460 560 400 C650 360 740 360 820 380 L820 490 L0 490 Z" fill="var(--brand-blue)"/>
    <path d="M430 440 C560 400 680 360 820 365 L820 380 C720 375 600 400 470 450 Z" fill="var(--deep-blue)"/>
    <path d="M640 380 C700 345 760 340 820 345 L820 365 C760 360 700 365 640 380 Z" fill="var(--oval)"/>
  </svg>

  <div class="abs brand">
    <span class="brand__dot"></span>
    <span class="brand__name">RK Cooling</span>
  </div>

  <div class="abs unit-art" role="img" aria-label="Photo of a split-system air conditioner with outdoor unit"></div>

  <div class="abs headline">
    <div class="headline__anniv">Celebrating <em>55 Years</em> Servicing</div>
    <div class="headline__region">The Chicago Suburbs</div>
    <div class="headline__season">Summer is Almost Here!</div>
    <p class="headline__lead">Make sure your system is running properly<br>and efficiently</p>
    <p class="headline__standard">The industry standard recommends an A/C<br>Clean &amp; Check <span>ONCE A YEAR</span></p>
  </div>

  <div class="abs benefits-band">Regular Preventive Maintenance Can:</div>
  <ul class="abs benefits">
    <li>Help Prolong the Life of your Equipment</li>
    <li>Help Lower Your Monthly Energy Costs</li>
    <li>Save Costs on Future Repairs</li>
  </ul>

  <div class="abs mention mention--front">Mention this Postcard and Take</div>
  <div class="abs offer offer--front"><b>$10.00</b>OFF</div>

  <div class="abs contact-bar">
    <span class="label">Call</span>
    <span>(555) 384-9120</span>
    <span>|</span>
    <span class="label">Address:</span>
    <span>718 Birchwood Ave. Marvale, IL</span>
  </div>
</section>

<section class="card card--back" aria-label="Postcard back">
  <div class="abs back-panel"></div>
  <svg class="abs swoosh" viewBox="0 0 820 540" aria-hidden="true">
    <path d="M0 340 C120 360 220 370 300 345 C350 330 390 320 410 318 L410 540 L0 540 Z" fill="var(--brand-blue)"/>
    <path d="M0 340 C60 345 110 352 150 358 L0 380 Z" fill="var(--bar)"/>
  </svg>

  <div class="abs since-band">Proudly Serving Chicagoland Area <em>Since 1961</em></div>
  <div class="abs services-title">We Also Service and Sell:</div>
  <ul class="abs services">
    <li>Coastline Prime Equipment.</li>
    <li>Brightvane Air Cleaners &amp; Humidifier Systems</li>
    <li>Hot Water Heaters, Boilers, and Digital Thermostats</li>
    <li>Residential and Commercial Fabrication Custom Welding</li>
  </ul>

  <div class="abs offer offer--back"><b>$10.00</b>OFF</div>
  <div class="abs mention mention--back">Mention this<br>Postcard and Take</div>
  <div class="abs schedule-band">Schedule Your Spring Clean &amp; Check Today!</div>
  <div class="abs back-contact">
    <span class="label">Phone:</span><span>(555) 384-9120</span>
    <span class="label">Mail:</span><span>rkcooling@mailnest.example</span>
    <span class="label">Website:</span><span>www.rkcoolingair.example</span>
  </div>

  <div class="abs divider"></div>
  <div class="abs stamp"></div>
  <div class="abs address-line" style="top:250px"></div>
  <div class="abs address-line" style="top:310px"></div>
  <div class="abs address-line" style="top:370px"></div>
</section>

</body>
</html>
```